Business Card Design Project

looking for a stylish and simple double sided business card.
I am an artist - specialising in fashion illustration, portraits and murals.
the front should be simply my name and tag:

D U R E S K
Art in every shade

My preference is for a Black background with DURESK in red or embossed.
Art in every shade in White or multi-coloured.

the back will have detail:

Personalised Art
Portraits, Murals, Fashion Illustration

0437 582 190
duresk@duresk.com.au
www.duresk.com.au

Target Market(s)

Adults that are based in western speaking countries who have an appreciation for art and design. Portraits and wall art
Business owners who may need personalised all art for their business space. Murals and personalised canvass.
People in the fashion industry, who may require fashion illustrations.

Industry/Entity Type

Fashion

Requirements
Must have
• BOLD but simple at the same time, timeless modern element to it.
Nice to have
• simple lettering
Should not have
• Not too busy or wordy,

```html
<!DOCTYPE html>
<html lang="en">
<head>
<meta charset="utf-8">
<title>Duresk — Business Card</title>
<link rel="stylesheet" href="https://fonts.googleapis.com/css2?family=Quicksand:wght@400;500;700&display=swap">
<style>
  :root {
    --backdrop: #e4e6ea;
    --card-dark: #2b2b2d;
    --card-light: #ffffff;
    --brand-red: #8c0f1c;
    --accent-grey: #3a3a3d;
    --pale-grey: #e1e3e6;
    --soft-grey: #b9bbc0;
    --ink: #3c3c44;
    --white: #ffffff;
  }
  * { box-sizing: border-box; margin: 0; padding: 0; }
  html, body {
    width: 1200px;
    height: 875px;
    overflow: hidden;
    background: var(--backdrop);
    font-family: "Quicksand", sans-serif;
  }
  .canvas {
    position: relative;
    width: 1200px;
    height: 875px;
    display: flex;
    align-items: center;
    justify-content: center;
    gap: 40px;
  }
  .card {
    position: relative;
    width: 540px;
    height: 330px;
    overflow: hidden;
    box-shadow: 0 6px 18px rgba(0, 0, 0, 0.12);
  }

  /* Front */
  .card--front { background: var(--card-dark); }
  .front__bar-red {
    position: absolute;
    top: 0; right: 0;
    width: 150px; height: 9px;
    background: var(--brand-red);
  }
  .front__bar-grey {
    position: absolute;
    top: 9px; right: 8px;
    width: 120px; height: 18px;
    background: var(--accent-grey);
  }
  .front__identity {
    position: absolute;
    left: 76px; top: 166px;
  }
  .front__name {
    font-weight: 500;
    font-size: 30px;
    letter-spacing: 0.04em;
    color: var(--white);
    line-height: 1.1;
  }
  .front__tagline {
    margin-top: 6px;
    font-weight: 400;
    font-size: 17px;
    color: var(--soft-grey);
  }

  /* Back */
  .card--back { background: var(--card-light); }
  .back__bar-top {
    position: absolute;
    top: 0; left: 250px;
    width: 200px; height: 16px;
    background: var(--pale-grey);
  }
  .back__services {
    position: absolute;
    top: 58px; right: 44px;
    text-align: right;
    text-transform: uppercase;
    font-weight: 400;
    font-size: 14.5px;
    letter-spacing: 0.02em;
    color: var(--ink);
    line-height: 2.1;
  }
  .back__dot {
    display: inline-block;
    width: 6px; height: 6px;
    margin: 0 6px 2px;
    background: var(--brand-red);
    vertical-align: middle;
  }
  .back__corner-square {
    position: absolute;
    right: 0; top: 168px;
    width: 26px; height: 26px;
    background: var(--brand-red);
  }
  .back__web {
    position: absolute;
    right: 40px; top: 214px;
    font-size: 14px;
    font-weight: 400;
    color: var(--brand-red);
  }
  .back__web strong { font-weight: 700; }
  .back__contact {
    position: absolute;
    left: 26px; bottom: 30px;
    font-size: 14.5px;
    color: var(--ink);
    line-height: 1.45;
  }
  .back__contact-row { display: flex; gap: 10px; }
  .back__label {
    width: 12px;
    font-weight: 700;
    color: var(--brand-red);
  }
</style>
</head>
<body>
<main class="canvas">
  <section class="card card--front" aria-label="Business card front">
    <div class="front__bar-red"></div>
    <div class="front__bar-grey"></div>
    <div class="front__identity">
      <h1 class="front__name">Duresk</h1>
      <p class="front__tagline">Art in every shade</p>
    </div>
  </section>

  <section class="card card--back" aria-label="Business card back">
    <div class="back__bar-top"></div>
    <div class="back__services">
      <p>Personalised Art<span class="back__dot"></span>Portraits</p>
      <p>Murals<span class="back__dot"></span>Fashion Illustration</p>
    </div>
    <div class="back__corner-square"></div>
    <p class="back__web">www.<strong>duresk</strong>.com.au</p>
    <div class="back__contact">
      <p class="back__contact-row"><span class="back__label">M</span>0437 582 190</p>
      <p class="back__contact-row"><span class="back__label">E</span>duresk@duresk.com.au</p>
    </div>
  </section>
</main>
</body>
</html>
```